Velno Recycling needs a new web design

We need a new web design for our company based in Austin, TX. We resell and recycling electronics such as laptops, computer components, Tovlets, Brunos, etc. Since our inception over ten years ago, we’ve become one of the premier electronics recycling and remarketing companies in Austin, Texas.

```html
<!DOCTYPE html>
<html lang="en">
<head>
<meta charset="utf-8">
<title>Velno Recycling</title>
<link href="https://fonts.googleapis.com/css2?family=Open+Sans:wght@400;600;700&display=swap" rel="stylesheet">
<style>
:root{
  --blue:#1a6fba;
  --blue-dark:#1460a8;
  --blue-footer:#1669bb;
  --ink:#333;
  --muted:#555;
  --grey-bg:#f1f0f1;
  --light-bg:#f6f7f9;
  --white:#fff;
}
*{margin:0;padding:0;box-sizing:border-box}
html,body{width:1200px;height:3930px;overflow:hidden;background:var(--white)}
body{font-family:"Open Sans",Arial,sans-serif;color:var(--ink);position:relative}
.abs{position:absolute}

.site-header{top:0;left:0;width:1200px;height:110px;background:var(--white)}
.brand{display:flex;align-items:center;gap:12px}
.brand-dot{width:56px;height:56px;border-radius:50%;background:var(--blue)}
.brand-name{font-weight:700;font-size:30px;color:var(--blue);letter-spacing:.5px}
.site-header .brand{position:absolute;left:100px;top:26px}
.contact-line{right:40px;top:26px;font-size:14px;color:var(--ink);display:flex;gap:28px}
.contact-line span::before{content:"";display:inline-block;width:10px;height:10px;background:var(--blue);border-radius:2px;margin-right:7px}
.main-nav{right:40px;top:62px;font-size:15px;display:flex;gap:22px}

.hero{top:110px;left:0;width:1200px;height:548px;background:linear-gradient(120deg,#3a3f44 0%,#6b6860 45%,#54534c 70%,#2f3236 100%)}
.hero-title{left:95px;top:138px;font-size:52px;line-height:62px;color:var(--white);font-weight:400;text-transform:uppercase}
.hero-sub{left:97px;top:268px;font-size:26px;color:var(--white);font-weight:600}
.btn{display:inline-flex;align-items:center;justify-content:center;font-size:15px;font-weight:600;text-transform:uppercase;letter-spacing:.5px}
.btn-solid{background:var(--blue);color:var(--white)}
.btn-outline{border:2px solid var(--white);color:var(--white)}
.hero .btn-solid{left:98px;top:330px;width:192px;height:48px}
.hero .btn-outline{left:320px;top:330px;width:192px;height:48px}
.hero-arrow{top:240px;width:36px;height:36px;border-radius:50%;background:rgba(255,255,255,.25)}

.section-title{width:1200px;left:0;text-align:center;font-size:32px;font-weight:700;color:var(--blue);text-transform:uppercase}
.pill{border-radius:24px;background:var(--blue);color:var(--white);font-size:15px;font-weight:600;display:flex;align-items:center;justify-content:center}
.about-text{left:283px;width:634px;top:792px;text-align:center;font-size:13.5px;line-height:28px;color:var(--muted)}

.wave-band{top:1000px;left:0}
.service-photo{border-radius:50%}
.service-title{font-size:32px;font-weight:700;color:var(--blue);text-transform:uppercase}
.service-sub{font-size:16px;font-weight:700;color:var(--blue)}
.service-text{font-size:13px;line-height:28px;color:var(--muted)}
.service-link{font-size:13px;color:var(--blue);text-decoration:underline}

.cap{width:260px;text-align:center}
.cap-icon{width:140px;height:140px;border-radius:50%;background:var(--blue);margin:0 auto;box-shadow:-6px 4px 0 #0d2f55;display:flex;align-items:center;justify-content:center}
.cap-name{margin-top:34px;font-size:17px;font-weight:700;color:var(--blue);text-transform:uppercase}
.cap-text{margin-top:8px;font-size:13px;line-height:24px;color:var(--ink)}

.contact-area{top:2935px;left:0;width:1200px;height:575px;background:var(--light-bg)}
.field{border:1.5px solid #888;background:transparent;font-size:13px;color:var(--ink);padding:14px 34px}

.site-footer{top:3510px;left:0;width:1200px;height:420px;background:var(--blue-footer)}
.footer-panel{left:97px;top:0;width:1003px;height:370px;background:#1a72c3}
.footer-nav{left:0;width:1200px;top:92px;display:flex;justify-content:center;gap:44px;font-size:13px;color:var(--white);text-transform:uppercase}
.site-footer .brand{left:0;width:1200px;top:138px;justify-content:center}
.site-footer .brand-dot{background:var(--white)}
.site-footer .brand-name{color:var(--white)}
.socials{left:0;width:1200px;top:258px;display:flex;justify-content:center;gap:22px}
.socials span{width:18px;height:18px;border-radius:50%;background:var(--white)}
.subscribe{left:447px;top:298px;display:flex}
.subscribe .email{width:193px;height:36px;background:var(--white);font-size:13px;padding:9px 14px;color:var(--ink)}
.subscribe .go{width:112px;height:36px;background:#c9cdd2;font-size:13px;display:flex;align-items:center;justify-content:center;color:var(--ink)}
.footer-rule{left:97px;top:370px;width:1003px;height:1px;background:rgba(255,255,255,.5)}
.copyright{left:0;width:1200px;top:387px;text-align:center;font-size:13px;color:var(--white)}
.code{right:40px;top:387px;font-size:13px;color:var(--white)}
</style>
</head>
<body>

<header class="site-header abs">
  <div class="brand"><span class="brand-dot"></span><span class="brand-name">Velno Recycling</span></div>
  <div class="contact-line abs"><span>hello@velnorecycling.com</span><span>(512) 555-0147</span></div>
  <nav class="main-nav abs"><span>Home</span><span>New Page</span><span>Book Online</span></nav>
</header>

<section class="hero abs" role="img" aria-label="Hands disassembling a computer circuit board with pliers on a workbench">
  <h1 class="hero-title abs">Computer Recycling<br>Made Easy</h1>
  <p class="hero-sub abs">Velno Recycling is here to help!</p>
  <span class="btn btn-solid abs">Purchase Now</span>
  <span class="btn btn-outline abs">Discover More</span>
  <span class="hero-arrow abs" style="left:10px"></span>
  <span class="hero-arrow abs" style="right:10px"></span>
</section>

<h2 class="section-title abs" style="top:730px">About Us</h2>
<p class="about-text abs">At Velno Recycling, we're committed to providing environmentally friendly recycling solutions to Austin and the surrounding areas. Founded in 2006, our mission is to process your materials in a safe, non-hazardous manner — with an aim to keep the world environmentally clean. As a R2 recycling center, we believe in promoting smart recycling habits in order to achieve long lasting results.</p>
<span class="pill abs" style="left:535px;top:930px;width:130px;height:45px">Read More</span>

<svg class="wave-band abs" width="1200" height="1390" viewBox="0 0 1200 1390">
  <path d="M0 90 C300 20 700 -10 1200 40 L1200 1270 C900 1390 400 1340 0 1290 Z" fill="#f1f0f1"/>
  <path d="M700 48 L1200 30 L1200 80 Z" fill="#1a6fba"/>
  <path d="M870 50 L1200 140 L1200 165 Z" fill="#1a6fba"/>
  <path d="M1080 45 L1200 37 L1200 62 Z" fill="#0d4f94"/>
</svg>

<div class="service-photo abs" style="left:-55px;top:1180px;width:640px;height:650px;background:radial-gradient(circle at 50% 70%,#3f7a3a 0%,#2f5a2c 40%,#6a5a52 75%,#3d3632 100%)" role="img" aria-label="Hands dropping old electronics into a green recycling bin"></div>
<h3 class="service-title abs" style="left:655px;top:1285px">Electronic Recycling</h3>
<p class="service-sub abs" style="left:655px;top:1327px">Environmentally Friendlya</p>
<p class="service-text abs" style="left:655px;top:1360px;width:390px">At Velno Recycling, we strive to keep the environment clean through our wide range of services. Our E-Waste Recycling services were designed to simplify the recycling process for residents in the Austin area. Contact us today and see how you can contribute to making this world a cleaner place.</p>
<span class="service-link abs" style="left:655px;top:1503px">Schedule A pick Up</span>

<div class="service-photo abs" style="left:608px;top:1577px;width:650px;height:650px;background:radial-gradient(circle at 50% 55%,#2f4fa8 0%,#3c8a3f 35%,#5b8a48 60%,#2d3a2a 100%)" role="img" aria-label="Blue bin being lifted into a green recycling truck"></div>
<h3 class="service-title abs" style="left:175px;top:1914px">Recycling Pickup</h3>
<p class="service-sub abs" style="left:175px;top:1955px">We Come To You</p>
<p class="service-text abs" style="left:175px;top:1988px;width:360px">At Velno Recycling, we go out of our way to make sure your recycling process is made easy as possible. Our Recycling Pickup service is designed to simplify all of your recycling needs. Take a look at all the services we offer and get in touch to see how you can start the process today!</p>
<span class="service-link abs" style="left:175px;top:2133px">Schedule A pick Up</span>

<h2 class="section-title abs" style="top:2425px">Our Capabilities</h2>
<div class="cap abs" style="left:64px;top:2534px">
  <div class="cap-icon"><svg width="70" height="44" viewBox="0 0 70 44"><rect x="2" y="4" width="40" height="28" fill="#fff"/><path d="M44 12 H58 L68 24 V32 H44 Z" fill="#fff"/><circle cx="16" cy="36" r="6" fill="#fff" stroke="#1a6fba" stroke-width="3"/><circle cx="56" cy="36" r="6" fill="#fff" stroke="#1a6fba" stroke-width="3"/></svg></div>
  <p class="cap-name">Logistics</p>
  <p class="cap-text">Lorem Ipsum is simply dummy text of the printing and typesetting indus tryorem Ipsum has be</p>
</div>
<div class="cap abs" style="left:334px;top:2534px">
  <div class="cap-icon"><svg width="60" height="56" viewBox="0 0 60 56"><path d="M30 6 L44 30 H16 Z" fill="none" stroke="#fff" stroke-width="6" stroke-linejoin="round"/><circle cx="30" cy="36" r="3" fill="#fff"/></svg></div>
  <p class="cap-name">Recycling</p>
  <p class="cap-text">Lorem Ipsum is simply dummy text of the printing and typesetting indus tryorem Ipsum has be</p>
</div>
<div class="cap abs" style="left:601px;top:2534px">
  <div class="cap-icon"><svg width="52" height="62" viewBox="0 0 52 62"><rect x="4" y="3" width="40" height="52" rx="3" fill="none" stroke="#fff" stroke-width="3"/><path d="M12 16H36M12 24H36M12 32H28" stroke="#fff" stroke-width="3"/><circle cx="38" cy="46" r="8" fill="#fff"/></svg></div>
  <p class="cap-name">Certificates</p>
  <p class="cap-text">Lorem Ipsum is simply dummy text of the printing and typesetting indus tryorem Ipsum has be</p>
</div>
<div class="cap abs" style="left:868px;top:2534px">
  <div class="cap-icon"><svg width="60" height="60" viewBox="0 0 60 60"><path d="M16 22 A18 18 0 1 1 14 38" fill="none" stroke="#fff" stroke-width="7"/><path d="M6 12 L20 12 L20 26 Z" fill="#fff"/></svg></div>
  <p class="cap-name">Return</p>
  <p class="cap-text">Lorem Ipsum is simply dummy text of the printing and typesetting indus tryorem Ipsum has be</p>
</div>

<section class="contact-area abs">
  <h2 class="section-title abs" style="top:72px">Get In Touch</h2>
  <div class="field abs" style="left:183px;top:158px;width:397px;height:47px">First Name</div>
  <div class="field abs" style="left:625px;top:158px;width:397px;height:47px">Last Name</div>
  <div class="field abs" style="left:183px;top:240px;width:397px;height:47px">Phone No</div>
  <div class="field abs" style="left:625px;top:240px;width:397px;height:47px">Email Id</div>
  <div class="field abs" style="left:183px;top:322px;width:839px;height:103px">Message</div>
  <span class="pill abs" style="left:535px;top:463px;width:130px;height:47px">Contact Us</span>
</section>

<footer class="site-footer abs">
  <div class="footer-panel abs"></div>
  <nav class="footer-nav abs"><span>About Us</span><span>Our Services</span><span>Our Purpose</span><span>Capabilitiess</span><span>Privacy &amp; Terms</span><span>Help</span><span>Contact Us</span></nav>
  <div class="brand abs"><span class="brand-dot"></span><span class="brand-name">Velno Recycling</span></div>
  <div class="socials abs"><span></span><span></span><span></span><span></span><span></span></div>
  <div class="subscribe abs"><span class="email">Enter Your Email</span><span class="go">Subscribe</span></div>
  <div class="footer-rule abs"></div>
  <p class="copyright abs">Copyright © 2018 velnorecycling.com. All Rights Reserved</p>
  <span class="code abs">C27</span>
</footer>

</body>
</html>
```